Payroll and Human Resources company needs Mailchimp Marketing Campaign

We need a Mailchimp marketing template to email prospective customers. We are an all-in-one solution for the entire employee lifecycle, including recruiting and hiring, payroll, human resources, and benefits administration. We save our customers time while ensuring they stay in compliance with labor laws and regulations. The email design should communicate that we are a local company offering big technology.

Target Market(s)

Small to mid-sized businesses

Industry/Entity Type

Human Resource

Font styles to use
Sans Serif

Colors
0455a3
acd136

Requirements
Must have
• Mention of services offered
Link to website: https://staffquillhub.com/
Nice to have
• Nice to have colors below to match logo

```html
<!DOCTYPE html>
<html lang="en">
<head>
<meta charset="utf-8">
<title>Staffquill Hub – Email Campaign</title>
<link href="https://fonts.googleapis.com/css2?family=Roboto:wght@400;500;700;900&family=Roboto+Condensed:wght@700&display=swap" rel="stylesheet">
<style>
  :root{
    --blue:#0455a3;
    --green:#acd136;
    --navy:#0b3560;
    --ink:#3a3f45;
    --muted:#6b7178;
    --page:#e4e4e4;
    --soft:#efefef;
    --white:#ffffff;
    --orange:#f29a2e;
    --amber:#f5c23a;
    --sky:#3fa9e0;
    --teal:#1aa39a;
    --red:#e2483d;
  }
  *{box-sizing:border-box;margin:0;padding:0}
  html,body{width:1200px;height:3208px;overflow:hidden}
  body{background:var(--page);font-family:"Roboto",Arial,sans-serif;color:var(--ink);position:relative}
  .email{position:absolute;left:320px;top:120px;width:560px;height:2992px;background:var(--white);box-shadow:0 6px 30px rgba(0,0,0,.18);overflow:hidden}
  .block{position:absolute;left:0;width:560px}

  /* header */
  .header{top:0;height:108px;display:flex;align-items:center;justify-content:space-between;padding:0 34px}
  .brand{display:flex;align-items:center;gap:10px;color:var(--blue);font-weight:700;font-size:16px;letter-spacing:.5px}
  .brand-dot{width:24px;height:24px;border-radius:50%;background:var(--green)}
  .call{color:var(--blue);font-family:"Roboto Condensed",sans-serif;font-weight:700;font-size:21px}

  /* hero */
  .hero{top:108px;height:260px}
  .hero-photo{position:absolute;inset:0;background:linear-gradient(120deg,#d7e3ec 0%,#9fb8cc 45%,#4f7597 100%)}
  .hero-panel{position:absolute;right:0;top:44px;width:292px;height:190px;background:rgba(172,209,54,.92);padding:26px 24px;color:var(--white)}
  .hero-title{font-family:"Roboto Condensed",sans-serif;font-size:22px;line-height:1.15;font-weight:700;letter-spacing:.3px}
  .hero-text{margin-top:12px;font-size:12.5px;line-height:1.5}

  /* about */
  .about{top:368px;height:224px;background:var(--soft)}
  .about-photo{position:absolute;left:40px;top:34px;width:200px;height:140px;background:linear-gradient(135deg,#c9ced3,#8b939b 60%,#5d666f)}
  .about-copy{position:absolute;left:288px;top:52px;width:240px}
  .section-title{font-family:"Roboto Condensed",sans-serif;font-weight:700;color:var(--blue);font-size:28px;letter-spacing:.5px}
  .about-copy p{margin-top:10px;font-size:12.5px;line-height:1.55;color:var(--muted)}

  /* services */
  .services{top:592px;height:1108px}
  .services .section-title{text-align:center;margin-top:40px}
  .rule{width:60px;height:3px;background:var(--green);margin:10px auto 0}
  .grid{position:absolute;left:34px;top:120px;width:492px;display:grid;grid-template-columns:repeat(3,1fr);gap:16px}
  .card{height:222px;border:1px solid #e3e6e9;border-radius:4px;background:var(--white);text-align:center;padding:22px 14px 0;box-shadow:0 2px 6px rgba(0,0,0,.05)}
  .card svg{width:48px;height:48px}
  .card h3{margin-top:12px;font-size:15px;font-weight:700;color:var(--blue);line-height:1.2}
  .card p{margin-top:8px;font-size:11px;line-height:1.5;color:var(--muted)}

  /* reporting */
  .reporting{top:1700px;height:340px}
  .reporting-bg{position:absolute;left:0;top:0;width:560px;height:180px;background:linear-gradient(180deg,#1b4f80 0%,var(--navy) 100%)}
  .reporting .section-title{position:absolute;top:30px;width:100%;text-align:center;color:var(--green)}
  .reporting p{position:absolute;top:74px;left:70px;width:420px;text-align:center;color:var(--white);font-size:12.5px;line-height:1.5}
  .dashboard{position:absolute;left:90px;top:150px;width:380px;height:180px;background:linear-gradient(180deg,#f6f8fa,#dfe5eb);border:6px solid #2c3238;border-radius:6px;box-shadow:0 8px 18px rgba(0,0,0,.2)}

  /* lifecycle */
  .lifecycle{top:2040px;height:440px}
  .lifecycle svg.ring{position:absolute;left:0;top:0}
  .stage{position:absolute;width:130px;font-size:10px;line-height:1.45;color:var(--muted)}
  .stage h4{font-size:12px;font-weight:700;letter-spacing:.5px;margin-bottom:3px}
  .ring-label{position:absolute;left:200px;top:226px;width:160px;text-align:center;font-family:"Roboto Condensed",sans-serif;font-weight:700;color:var(--muted);font-size:16px;line-height:1.1;letter-spacing:.5px}

  /* help bar */
  .help{top:2480px;height:72px;background:var(--green);display:flex;align-items:center;justify-content:center;gap:14px;color:var(--navy)}
  .help span{font-family:"Roboto Condensed",sans-serif;font-weight:700;font-size:15px;line-height:1.2;letter-spacing:.3px}

  /* footer */
  .footer{top:2552px;height:440px;background:var(--navy);color:var(--white);text-align:center}
  .pin{margin-top:44px}
  .address{margin-top:16px;font-weight:700;font-size:16px;line-height:1.45}
  .social{margin-top:28px;display:flex;justify-content:center;gap:18px}
  .social span{width:28px;height:28px;border-radius:50%;background:var(--white)}
  .site{display:block;margin-top:30px;color:var(--green);font-weight:700;font-size:15px;text-decoration:none}
  .divider{width:480px;height:1px;background:rgba(255,255,255,.25);margin:40px auto 0}
  .copyright{margin-top:32px;font-size:11px;color:rgba(255,255,255,.7)}
</style>
</head>
<body>
<main class="email">

  <header class="block header">
    <div class="brand"><span class="brand-dot"></span>STAFFQUILL HUB</div>
    <div class="call">CALL:225-555-0148</div>
  </header>

  <section class="block hero">
    <div class="hero-photo" role="img" aria-label="Photo of two colleagues working together at a laptop in a bright office"></div>
    <div class="hero-panel">
      <h1 class="hero-title">STAFFQUILL HUB</h1>
      <p class="hero-text">Staffquill Hub has been providing companies with human capital management solutions since 1996.</p>
    </div>
  </section>

  <section class="block about">
    <div class="about-photo" role="img" aria-label="Photo of a hand placing a gear among interlocking gears"></div>
    <div class="about-copy">
      <h2 class="section-title">ABOUT US</h2>
      <p>We are a local company offering big technology, helping small and mid-sized businesses handle payroll, HR and benefits while staying compliant.</p>
    </div>
  </section>

  <section class="block services">
    <h2 class="section-title">SERVICES OFFERED</h2>
    <div class="rule"></div>
    <div class="grid">
      <div class="card">
        <svg viewBox="0 0 48 48" fill="none" stroke="#acd136" stroke-width="3"><rect x="6" y="12" width="36" height="24" rx="3"/><circle cx="24" cy="24" r="6"/></svg>
        <h3>Payroll</h3><p>Accurate payroll runs, tax filings and direct deposit every pay period.</p>
      </div>
      <div class="card">
        <svg viewBox="0 0 48 48" fill="none" stroke="#acd136" stroke-width="3"><circle cx="24" cy="16" r="7"/><path d="M10 40c2-9 8-13 14-13s12 4 14 13"/></svg>
        <h3>COBRA</h3><p>Assist with qualifying events, notices and COBRA administration for your team.</p>
      </div>
      <div class="card">
        <svg viewBox="0 0 48 48" fill="none" stroke="#acd136" stroke-width="3"><rect x="10" y="6" width="28" height="36" rx="2"/><path d="M24 16v14M17 23h14"/></svg>
        <h3>HRA</h3><p>Flexible health reimbursement plans set up and administered for you.</p>
      </div>
      <div class="card">
        <svg viewBox="0 0 48 48" fill="none" stroke="#acd136" stroke-width="3"><rect x="8" y="10" width="32" height="28" rx="2"/><path d="M14 20h20M14 28h14"/></svg>
        <h3>Benefits Administration</h3><p>Manage enrollment, carriers and employee benefit changes in one place.</p>
      </div>
      <div class="card">
        <svg viewBox="0 0 48 48" fill="none" stroke="#acd136" stroke-width="3"><circle cx="17" cy="17" r="6"/><circle cx="32" cy="19" r="5"/><path d="M6 38c1-7 6-11 11-11s10 4 11 11M28 30c2-3 4-4 6-4 4 0 7 4 8 10"/></svg>
        <h3>HR Assist</h3><p>Certified HR advisors on call to answer your daily questions.</p>
      </div>
      <div class="card">
        <svg viewBox="0 0 48 48" fill="none" stroke="#acd136" stroke-width="3"><circle cx="24" cy="24" r="8"/><path d="M24 6v6M24 36v6M6 24h6M36 24h6M11 11l4 4M33 33l4 4M11 37l4-4M33 15l4-4"/></svg>
        <h3>HR Manage</h3><p>Full outsourced HR support that keeps policies current and compliant.</p>
      </div>
      <div class="card">
        <svg viewBox="0 0 48 48" fill="none" stroke="#acd136" stroke-width="3"><circle cx="24" cy="24" r="17"/><path d="M24 13v11l8 5"/></svg>
        <h3>Time and Attendance</h3><p>Track hours, breaks and time off with simple online clocks.</p>
      </div>
      <div class="card">
        <svg viewBox="0 0 48 48" fill="none" stroke="#acd136" stroke-width="3"><rect x="8" y="8" width="32" height="32" rx="3"/><path d="M15 25l6 6 12-13"/></svg>
        <h3>ATS</h3><p>Post jobs, screen applicants and hire faster with smart tracking.</p>
      </div>
      <div class="card">
        <svg viewBox="0 0 48 48" fill="none" stroke="#acd136" stroke-width="3"><ellipse cx="24" cy="12" rx="14" ry="5"/><path d="M10 12v24c0 3 6 5 14 5s14-2 14-5V12M10 24c0 3 6 5 14 5s14-2 14-5"/></svg>
        <h3>HRIS</h3><p>Keep employee records secure and organized in one central system.</p>
      </div>
      <div class="card">
        <svg viewBox="0 0 48 48" fill="none" stroke="#acd136" stroke-width="3"><rect x="10" y="6" width="28" height="36" rx="2"/><path d="M16 16h16M16 23h16M16 30h10"/></svg>
        <h3>Labor Law Posters</h3><p>Stay current with required federal and state workplace posters.</p>
      </div>
      <div class="card">
        <svg viewBox="0 0 48 48" fill="none" stroke="#acd136" stroke-width="3"><path d="M8 40V28M18 40V20M28 40V24M38 40V10M6 40h36"/></svg>
        <h3>Onboarding</h3><p>Paperless new hire forms that get employees ready on day one.</p>
      </div>
      <div class="card">
        <svg viewBox="0 0 48 48" fill="none" stroke="#acd136" stroke-width="3"><circle cx="24" cy="24" r="16"/><path d="M24 14v20M14 24h20"/></svg>
        <h3>Affirmative Action</h3><p>Plans and reporting that support your equal opportunity goals.</p>
      </div>
    </div>
  </section>

  <section class="block reporting">
    <div class="reporting-bg" role="img" aria-label="Dark blue tinted photo of a team meeting"></div>
    <h2 class="section-title">REPORTING</h2>
    <p>When you need payroll support and compliance, we offer standard online payroll services. We provide a comprehensive and quality service that is accessible in one easy-to-use platform.</p>
    <div class="dashboard" role="img" aria-label="Screenshot of the online reporting dashboard on a laptop screen"></div>
  </section>

  <section class="block lifecycle">
    <svg class="ring" width="560" height="440" viewBox="0 0 560 440" fill="none">
      <g transform="rotate(-90 280 240)" stroke-width="7" stroke-linecap="round">
        <circle cx="280" cy="240" r="88" stroke="#f29a2e" stroke-dasharray="80 473"/>
        <circle cx="280" cy="240" r="88" stroke="#f5c23a" stroke-dasharray="80 473" stroke-dashoffset="-92"/>
        <circle cx="280" cy="240" r="88" stroke="#3fa9e0" stroke-dasharray="80 473" stroke-dashoffset="-184"/>
        <circle cx="280" cy="240" r="88" stroke="#1aa39a" stroke-dasharray="80 473" stroke-dashoffset="-276"/>
        <circle cx="280" cy="240" r="88" stroke="#0455a3" stroke-dasharray="80 473" stroke-dashoffset="-368"/>
        <circle cx="280" cy="240" r="88" stroke="#e2483d" stroke-dasharray="80 473" stroke-dashoffset="-460"/>
      </g>
      <circle cx="280" cy="240" r="72" stroke="#d6dadf" stroke-width="1"/>
      <g stroke-width="1.5">
        <path d="M320 160 L340 80 H360" stroke="#f29a2e"/>
        <path d="M366 220 H420" stroke="#f5c23a"/>
        <path d="M350 300 L400 330 H420" stroke="#3fa9e0"/>
        <path d="M280 330 V360" stroke="#1aa39a"/>
        <path d="M200 290 L150 320 H140" stroke="#0455a3"/>
        <path d="M214 180 L160 150 H140" stroke="#e2483d"/>
      </g>
    </svg>
    <div class="ring-label">EMPLOYEE<br>LIFECYCLE</div>
    <div class="stage" style="left:364px;top:46px"><h4 style="color:var(--orange)">ONBOARDING</h4>Welcome new hires with guided paperwork and training.</div>
    <div class="stage" style="left:424px;top:196px"><h4 style="color:var(--amber)">PAYROLL</h4>Pay employees on time with accurate tax filing.</div>
    <div class="stage" style="left:424px;top:316px"><h4 style="color:var(--sky)">BENEFITS</h4>Offer competitive plans and easy open enrollment.</div>
    <div class="stage" style="left:215px;top:364px;text-align:center"><h4 style="color:var(--teal)">EMPLOYEE MANAGEMENT</h4>Track performance, reviews and time off.</div>
    <div class="stage" style="left:14px;top:308px"><h4 style="color:var(--blue)">SEPARATION</h4>Handle exits, final pay and COBRA notices.</div>
    <div class="stage" style="left:14px;top:120px"><h4 style="color:var(--red)">HIRING</h4>Find and screen qualified candidates quickly.</div>
  </section>

  <section class="block help">
    <svg width="30" height="30" viewBox="0 0 24 24" fill="#0b3560"><path d="M6.6 10.8a15.1 15.1 0 0 0 6.6 6.6l2.2-2.2a1 1 0 0 1 1-.25 11.4 11.4 0 0 0 3.6.57 1 1 0 0 1 1 1V20a1 1 0 0 1-1 1A17 17 0 0 1 3 4a1 1 0 0 1 1-1h3.5a1 1 0 0 1 1 1c0 1.25.2 2.45.57 3.57a1 1 0 0 1-.25 1z"/></svg>
    <span>NEED HELP? CALL OUR AWESOME<br>&amp; SUPPORT TEAM AT 225-555-0148</span>
  </section>

  <footer class="block footer">
    <svg class="pin" width="30" height="38" viewBox="0 0 24 30" fill="#acd136"><path d="M12 0C5.4 0 0 5.2 0 11.7 0 20.5 12 30 12 30s12-9.5 12-18.3C24 5.2 18.6 0 12 0zm0 16a4.5 4.5 0 1 1 0-9 4.5 4.5 0 0 1 0 9z"/></svg>
    <p class="address">4127 Maplecrest Drive<br>Baton Rouge, LA 70816</p>
    <div class="social"><span></span><span></span></div>
    <a class="site" href="https://staffquillhub.com/">https://staffquillhub.com/</a>
    <div class="divider"></div>
    <p class="copyright">© 2024 All rights reserved.</p>
  </footer>

</main>
</body>
</html>
```